Labels/logo for luxury bath products

I am developing a range of luxury bath foams - aimed at the top end of the luxury market. My company name is VRE (very basic website can be seen at www.vremarket.example).

I am looking for a label design for the front of the bottle, which should incorporate the VRE logo as per the website (file attached), but embedded within a more intricate label design. I provide a link to a picture of the bottle below.

The bath foam will come in four fragrances: Vetiver, Sandalwood, Jasmine and Neroli. The label should include the fragrance name. So the label must include the brand name 'VRE' and the name of the fragrance - e.g. Sandalwood Bath Foam, Neroli Bath Foam, etc.

The products are aimed at both the male and female market and so shouldn't be too feminine.

A brand to take inspiration from is Mabel Fenwick: http://www.mabelfenwick.example/ - I like the labels that they use on their products, which is a gold embossed crest, which they use as the label for their products. I am not referring to their font, but to their label design - I like the embossed label, and am quite keen on metallics.

Conversely, I would like to add a contemporary edge to this design - I like the striping and contemporary fonts on this design: http://www.tamsin-gale.example/images/qbx41.jpg

My brand also harnesses the powers of natural flower ingredients, and so I am inspired by the products of Ylvane - ylvane.example. This labelling is more clinical and scientific.

Ideally I would like a label which combines these elements - i.e. a luxury label with a contemporary feel, that incorporate the scientific nature of the product.

The design needs to communicate high end luxury. The bottle is however apothecary style, and a nod to science and botany would be good. I would however like a bold approach to this design - it is a modern brand.

The bottle being used for the product can be seen at: http://www.brevik-flask.example/en/product-groups/8-Apothecary-bottles - these are extremely expensive bottles and the label needs to reflect this quality. These bottles are traditional in design, but incorporate high end glassware technology to preserve the integrity of the natural ingredients. Therefore the product is a mix of old and new, and the label could also reflect this. The colour of the glass is very deep purple.

The front label does not need information such as weight/volume - it purely needs a label which will recognise it as the VRE brand, with the product name. I am looking for a high quality label, which is unique. I am happy to print embossed labels and to use foils on my labels.

Please do not be boring! I appreciate I have given a variety of influences, so summarise the requirements are a mix of:

a bold design
contemporary
luxury

The label must include NO slogans.

I am looking to build a relationship with a graphic designer for packaging and website design requirements so this will be the first of many projects.

Target Market(s)

Luxury end of market - clientele will like luxury and will pay for the highest quality ingredients in the product, but will also appreciate the botanical nature of the product.

Industry/Entity Type

Graphic Designer

Requirements
Must have
• Must include the company name, VRE, although this doesn't need to be particularly prominent. And the product name, e.g. Sandalwood.
Nice to have
• It should combine luxury, but with recognition of the science behind the product.
Should not have
• No slogans, minimal wording on the front label. No other wording other than company name and product name. No primary colours.

```html
<!DOCTYPE html>
<html lang="en">
<head>
<meta charset="utf-8">
<title>VRE Sandalwood Bath Foam Label</title>
<link rel="stylesheet" href="https://fonts.googleapis.com/css2?family=Cinzel:wght@400;700&display=swap">
<style>
  :root {
    --page: #ffffff;
    --gold-dark: #9c8448;
    --gold-mid: #c9b57a;
    --gold-light: #f1ead0;
    --navy-deep: #02031f;
    --navy-band: #0b2463;
    --panel-edge: #a99a68;
    --panel-mid: #d4c89e;
    --panel-light: #f1ecd2;
    --brand-ink: #8a6f2e;
    --name-ink: #6f5e33;
  }
  html, body {
    margin: 0;
    padding: 0;
    width: 1200px;
    height: 1149px;
    overflow: hidden;
    background: var(--page);
  }
  .label-canvas {
    display: block;
    width: 1200px;
    height: 1149px;
  }
  .brand-name {
    font-family: "Cinzel", serif;
    font-weight: 700;
    font-size: 172px;
    fill: var(--brand-ink);
    letter-spacing: 2px;
  }
  .product-name {
    font-family: "Cinzel", serif;
    font-weight: 400;
    fill: var(--name-ink);
  }
  .product-name--fragrance { font-size: 30px; }
  .product-name--type { font-size: 35px; }
</style>
</head>
<body>
<svg class="label-canvas" viewBox="0 0 1000 958" xmlns="http://www.w3.org/2000/svg">
  <defs>
    <linearGradient id="frameGold" x1="0" y1="0" x2="1" y2="0">
      <stop offset="0" stop-color="var(--gold-dark)"/>
      <stop offset="0.5" stop-color="var(--gold-light)"/>
      <stop offset="1" stop-color="var(--gold-dark)"/>
    </linearGradient>
    <linearGradient id="panelGold" x1="0" y1="0" x2="1" y2="0">
      <stop offset="0" stop-color="var(--panel-edge)"/>
      <stop offset="0.5" stop-color="var(--panel-light)"/>
      <stop offset="1" stop-color="var(--panel-edge)"/>
    </linearGradient>
    <pattern id="navyStripes" width="60" height="60" patternUnits="userSpaceOnUse" patternTransform="rotate(-20)">
      <rect width="60" height="60" fill="var(--navy-deep)"/>
      <rect width="60" height="26" fill="var(--navy-band)"/>
    </pattern>
  </defs>

  <path class="label-frame"
        d="M262,220 C262,110 360,45 471,45 C582,45 680,110 680,220 L712,220 L712,272 C770,300 805,370 805,440 C805,510 770,580 712,608 L712,695 L680,695 C680,810 582,915 471,915 C360,915 262,810 262,695 L228,695 L228,608 C170,580 138,510 138,440 C138,370 170,300 228,272 L228,220 Z"
        fill="url(#frameGold)"/>

  <path class="label-band"
        d="M282,236 C282,128 372,68 471,68 C570,68 660,128 660,236 L695,236 L695,285 C748,312 783,375 783,440 C783,505 748,568 695,595 L695,680 L660,680 C660,792 570,892 471,892 C372,892 282,792 282,680 L246,680 L246,595 C193,568 160,505 160,440 C160,375 193,312 246,285 L246,236 Z"
        fill="url(#navyStripes)"/>

  <path class="label-panel" role="img" aria-label="Embossed gold panel with a fine honeycomb texture"
        d="M318,250 C318,170 385,118 471,118 C557,118 622,170 622,250 L622,285 L650,285 L650,322 C705,340 735,390 735,440 C735,495 705,545 650,565 L650,645 L622,645 L622,720 C622,800 557,850 471,850 C385,850 318,800 318,720 L318,645 L290,645 L290,565 C237,545 207,495 207,440 C207,390 237,340 290,322 L290,285 L318,285 Z"
        fill="url(#panelGold)"/>

  <text class="brand-name" x="478" y="516" text-anchor="middle">VRE</text>

  <text class="product-name product-name--fragrance" x="463" y="708" text-anchor="middle">SANDALWOOD</text>
  <text class="product-name product-name--type" x="463" y="752" text-anchor="middle">BATH FOAM</text>
</svg>
</body>
</html>
```